Medical Transportation Company Brochure

I need a brochure for a medical transportation company called CareSwift Transit Health Services that provides ambulance and mobility assistance vehicle transportation services to and from healthcare facilities as well as event standby and healthcare training through our training center (cpr, professional continuing education courses). Id like something that incorporates our company logo's colors and looks eye catching yet sleek and professional

Target Market(s)

Patients, healthcare facilities

Industry/Entity Type

Medical

Font styles to use
Sans Serif

Requirements
Must have
• Flyer must have a description of our services as well as text that is easy to read, be visually captivating and stand out, include our contact information and process to book appointment for transport with us

```html
<!DOCTYPE html>
<html lang="en">
<head>
<meta charset="utf-8">
<title>CareSwift Transit Health Services – Trifold Brochure</title>
<link href="https://fonts.googleapis.com/css2?family=Bebas+Neue&family=Lato:wght@400;700;900&family=Raleway:wght@400;500&display=swap" rel="stylesheet">
<style>
  :root {
    --navy: #1b3470;
    --navy-deep: #152a5c;
    --red: #c8102e;
    --paper: #f4f4f5;
    --panel-grey: #dcdde0;
    --ink: #2a2d33;
    --white: #ffffff;
  }
  * { box-sizing: border-box; margin: 0; padding: 0; }
  html, body { width: 1200px; height: 900px; overflow: hidden; background: var(--paper); }
  .brochure { display: flex; width: 1200px; height: 900px; }
  .panel { position: relative; width: 400px; height: 900px; overflow: hidden; }

  .display { font-family: "Bebas Neue", "Arial Narrow", sans-serif; font-weight: 400; line-height: 0.95; color: var(--navy); }
  .display .accent { color: var(--red); }
  .photo { position: absolute; }

  /* Left panel */
  .panel--intro { background: var(--paper); }
  .intro-band { position: absolute; left: 0; top: 0; width: 400px; height: 364px; background: linear-gradient(135deg, var(--navy) 0%, var(--navy-deep) 100%); }
  .intro-title { position: absolute; left: 16px; top: 16px; font-size: 56px; color: var(--white); letter-spacing: -0.5px; }
  .intro-lead { position: absolute; left: 16px; top: 86px; width: 372px; font-family: "Raleway", sans-serif; font-size: 17.5px; line-height: 27px; color: var(--white); }
  .photo--escort { left: 16px; top: 187px; width: 384px; height: 297px; background: linear-gradient(120deg, #8fa0b8 0%, #3b5a9a 40%, #c9d2dc 75%, #e9ecef 100%); }
  .best-title { position: absolute; left: 16px; top: 508px; font-size: 58px; letter-spacing: -0.5px; }
  .body-copy { font-family: "Lato", sans-serif; font-size: 17px; line-height: 27.5px; color: var(--ink); }
  .best-copy { position: absolute; left: 16px; top: 570px; width: 372px; }
  .best-copy p + p { margin-top: 26px; }

  /* Middle panel */
  .panel--contact { background: var(--panel-grey); }
  .contact-band { position: absolute; left: 0; top: 0; width: 400px; height: 16px; background: var(--navy); }
  .photo--street { left: 17px; top: 14px; width: 365px; height: 476px; background: linear-gradient(160deg, #8a4a3a 0%, #6e3a30 40%, #3a3a44 70%, #23252c 100%); }
  .contact-title { position: absolute; left: 63px; top: 536px; font-size: 70px; letter-spacing: -0.5px; }
  .contact-list { position: absolute; left: 64px; top: 628px; list-style: none; }
  .contact-item { display: flex; align-items: flex-start; gap: 22px; margin-bottom: 26px; }
  .contact-item svg { width: 34px; height: 34px; flex: none; margin-top: 4px; fill: var(--navy); }
  .contact-text { font-family: "Lato", sans-serif; font-size: 20px; line-height: 26px; color: var(--ink); }
  .contact-text sup { font-size: 11px; }

  /* Right panel */
  .panel--cover { background: var(--paper); }
  .cover-band { position: absolute; left: 0; top: 0; width: 400px; height: 370px; background: var(--navy); }
  .photo--vehicle { left: 0; top: 14px; width: 376px; height: 397px; background: linear-gradient(110deg, #9aa3ad 0%, #e7eaee 40%, #c8cdd3 60%, #b3262f 66%, #8d949c 80%, #5c636b 100%); }
  .cover-title { position: absolute; left: 16px; top: 448px; font-size: 70px; line-height: 60px; letter-spacing: -1.5px; }
  .cover-copy { position: absolute; left: 16px; top: 642px; width: 374px; font-family: "Lato", sans-serif; font-size: 18px; line-height: 28px; color: var(--ink); }
  .brand { position: absolute; left: 36px; top: 790px; display: flex; align-items: center; gap: 12px; }
  .brand-dot { width: 40px; height: 40px; border-radius: 50%; background: var(--navy); }
  .brand-name { font-family: "Lato", sans-serif; font-weight: 900; font-size: 40px; color: var(--navy); letter-spacing: -0.5px; }
  .brand-tagline { position: absolute; left: 88px; top: 840px; font-family: "Lato", sans-serif; font-size: 12px; letter-spacing: 0.5px; color: var(--navy); }
</style>
</head>
<body>
<main class="brochure">

  <section class="panel panel--intro">
    <div class="intro-band"></div>
    <h2 class="display intro-title">We Help To Grow</h2>
    <p class="intro-lead">From routine checkups to urgent transfers, our trained crews get every patient where they need to be, safely.</p>
    <div class="photo photo--escort" role="img" aria-label="Photo of a motorcycle escort rider beside a runner at a road race event"></div>
    <h2 class="display best-title">We Are <span class="accent">Best</span></h2>
    <div class="body-copy best-copy">
      <p>Our fleet covers ambulance runs, wheelchair and mobility assistance vans, plus event standby crews for races, concerts and community gatherings.</p>
      <p>Booking is simple: call or email us, share pickup and facility details, then receive your confirmed time. Our training center also runs CPR and continuing education courses.</p>
    </div>
  </section>

  <section class="panel panel--contact">
    <div class="contact-band"></div>
    <div class="photo photo--street" role="img" aria-label="Photo of ambulances and a cyclist on a busy city street lined with brick buildings"></div>
    <h2 class="display contact-title">Get In <span class="accent">Touch</span></h2>
    <ul class="contact-list">
      <li class="contact-item">
        <svg viewBox="0 0 24 24" aria-hidden="true"><path d="M6.6 10.8a15.1 15.1 0 0 0 6.6 6.6l2.2-2.2a1 1 0 0 1 1-.25 11.4 11.4 0 0 0 3.6.57 1 1 0 0 1 1 1V20a1 1 0 0 1-1 1A17 17 0 0 1 3 4a1 1 0 0 1 1-1h3.5a1 1 0 0 1 1 1c0 1.25.2 2.45.57 3.57a1 1 0 0 1-.25 1z"/></svg>
        <div class="contact-text">+1 555 014 2290<br>+1 555 014 2291</div>
      </li>
      <li class="contact-item">
        <svg viewBox="0 0 24 24" aria-hidden="true"><path d="M12 2a10 10 0 1 0 0 20 10 10 0 0 0 0-20zm6.9 6h-2.9a15.6 15.6 0 0 0-1.4-3.6A8 8 0 0 1 18.9 8zM12 4a14 14 0 0 1 1.9 4h-3.8A14 14 0 0 1 12 4zM4.3 14a8.2 8.2 0 0 1 0-4h3.4a16.5 16.5 0 0 0 0 4zm.8 2h2.9a15.6 15.6 0 0 0 1.4 3.6A8 8 0 0 1 5.1 16zM8 8H5.1a8 8 0 0 1 4.3-3.6A15.6 15.6 0 0 0 8 8zm4 12a14 14 0 0 1-1.9-4h3.8A14 14 0 0 1 12 20zm2.3-6H9.7a14.7 14.7 0 0 1 0-4h4.6a14.7 14.7 0 0 1 0 4zm.3 5.6a15.6 15.6 0 0 0 1.4-3.6h2.9a8 8 0 0 1-4.3 3.6zm1.7-5.6a16.5 16.5 0 0 0 0-4h3.4a8.2 8.2 0 0 1 0 4z"/></svg>
        <div class="contact-text">hello@careswift.com<br>www.careswift.com</div>
      </li>
      <li class="contact-item">
        <svg viewBox="0 0 24 24" aria-hidden="true"><path d="M12 3 2 12h3v9h5v-6h4v6h5v-9h3z"/></svg>
        <div class="contact-text">48 Harbor Lane, 3<sup>rd</sup> Floor,<br>Riverton, NY 10482</div>
      </li>
    </ul>
  </section>

  <section class="panel panel--cover">
    <div class="cover-band"></div>
    <div class="photo photo--vehicle" role="img" aria-label="Photo of a white ambulance van with red and blue stripes driving at speed"></div>
    <h1 class="display cover-title">Mobile Health<br>Services <span class="accent">That</span><br><span class="accent">Provides.</span></h1>
    <p class="cover-copy">CareSwift Transit Health Services provides ambulance and mobility assistance vehicle transportation to and from healthcare facilities.</p>
    <div class="brand">
      <span class="brand-dot"></span>
      <span class="brand-name">CareSwift</span>
    </div>
    <div class="brand-tagline">TRANSIT HEALTH SERVICES</div>
  </section>

</main>
</body>
</html>
```